New Business card design to reflect rebrand

I would like a business card design with a good base colour for our new logo and also a placeholder for a profile pic of the card holder. the design needs to be editable to the point that we can easily change the picture of the person and use that design for printlarkly etc. we are looking at a metalic finish business card so will need a good base colour to bring out the finish.

Target Market(s)

prospective customers

Industry/Entity Type

Business

Contact Information for Business Card

I would like one editable design that we can change the name of the card holder and profile picture. The design need to be in a format that be send to printlarkly etc.

Our address is Fenwick Lodge, Mill Lane, Hartley Wintney, KT14 3WB Tel no. 01632 960418

Requirements
Must have
• place holder for a profile pic for the card holder. in AI or preferably PSD format

```html
<!DOCTYPE html>
<html lang="en">
<head>
<meta charset="utf-8">
<title>Lumark Workplace Services – Business Card</title>
<link rel="stylesheet" href="https://fonts.googleapis.com/css2?family=Questrial&display=swap">
<style>
  :root {
    --navy: #2c3e5c;
    --navy-deep: #1f2d47;
    --navy-back: #2a3a58;
    --orange: #f26f21;
    --silver-light: #e9eaec;
    --silver-mid: #c9cbcf;
    --silver-dark: #a9acb1;
    --white: #ffffff;
    --stage: #ffffff;
  }
  * { margin: 0; padding: 0; box-sizing: border-box; }
  html, body { width: 1200px; height: 900px; overflow: hidden; }
  body {
    background: var(--stage);
    font-family: "Questrial", "Century Gothic", sans-serif;
    display: flex;
    align-items: center;
    justify-content: center;
    gap: 44px;
  }
  .card {
    position: relative;
    width: 540px;
    height: 310px;
    border-radius: 22px;
    overflow: hidden;
    box-shadow: 0 10px 24px rgba(0,0,0,0.18);
  }

  /* Front */
  .card-front { background: var(--navy); }
  .front-top {
    position: absolute; inset: 0 0 auto 0; height: 168px;
    background:
      repeating-linear-gradient(180deg, rgba(255,255,255,0.18) 0 1px, transparent 1px 3px),
      linear-gradient(180deg, var(--silver-light) 0%, var(--silver-mid) 60%, var(--silver-dark) 100%);
  }
  .front-rule {
    position: absolute; left: 0; right: 0; top: 168px; height: 6px;
    background: var(--orange);
  }
  .front-bottom {
    position: absolute; left: 0; right: 0; top: 174px; bottom: 0;
    background:
      repeating-linear-gradient(180deg, rgba(255,255,255,0.04) 0 1px, transparent 1px 3px),
      linear-gradient(90deg, var(--navy-deep), var(--navy));
  }
  .brand {
    position: absolute; left: 28px; top: 46px;
    display: flex; align-items: center; gap: 12px;
    color: var(--navy);
  }
  .brand-dot { width: 40px; height: 40px; border-radius: 50%; background: var(--navy); flex: none; }
  .brand-name { font-size: 30px; line-height: 1.05; letter-spacing: 0.5px; }
  .brand-name span { display: block; font-size: 16px; letter-spacing: 2.4px; }

  .holder {
    position: absolute; right: 26px; top: 30px; text-align: right;
  }
  .holder-name { color: var(--orange); font-size: 21px; }
  .holder-role { color: var(--navy); font-size: 13px; margin-top: 6px; }

  .portrait {
    position: absolute; right: 0; bottom: 0; width: 170px; height: 198px;
    background: linear-gradient(180deg, #6b5a58 0%, #4a4350 55%, #2a2630 100%);
  }

  .contact {
    position: absolute; left: 24px; top: 190px;
    list-style: none; color: var(--white); font-size: 13.5px;
  }
  .contact li { display: flex; align-items: center; gap: 6px; height: 19px; }
  .contact svg { width: 12px; height: 12px; flex: none; fill: var(--orange); }

  /* Back */
  .card-back {
    background:
      repeating-linear-gradient(180deg, rgba(255,255,255,0.035) 0 1px, transparent 1px 3px),
      linear-gradient(90deg, var(--navy-back), var(--navy-deep));
    display: flex; align-items: center; justify-content: center;
  }
  .back-brand { font-size: 56px; letter-spacing: 3px; color: #3a4d70; }
</style>
</head>
<body>
  <section class="card card-front" aria-label="Business card front">
    <div class="front-top"></div>
    <div class="front-rule"></div>
    <div class="front-bottom"></div>

    <div class="brand">
      <div class="brand-dot"></div>
      <div class="brand-name">LUMARK<span>WORKPLACE SERVICES</span></div>
    </div>

    <div class="holder">
      <div class="holder-name">Dana Mercer VP</div>
      <div class="holder-role">Manager</div>
    </div>

    <div class="portrait" role="img" aria-label="Profile photo of the card holder"></div>

    <ul class="contact">
      <li><svg viewBox="0 0 12 12"><rect x="3" y="0.5" width="6" height="11" rx="1"/></svg>555-014-2290</li>
      <li><svg viewBox="0 0 12 12"><path d="M2 1l2.5 0 1 3-1.5 1a7 7 0 0 0 3 3l1-1.5 3 1V10a1.5 1.5 0 0 1-1.5 1.5A10 10 0 0 1 .5 2.5 1.5 1.5 0 0 1 2 1z"/></svg>555-014-2291</li>
      <li><svg viewBox="0 0 12 12"><path d="M0.5 3h11v7h-11z M0.5 3l5.5 4 5.5-4" stroke="#f26f21" stroke-width="1" fill="none"/></svg>dana@lumarkworkplace.com</li>
      <li><svg viewBox="0 0 12 12"><circle cx="6" cy="6" r="5" fill="none" stroke="#f26f21" stroke-width="1.2"/><path d="M1 6h10M6 1v10" stroke="#f26f21" stroke-width="1"/></svg>www.lumarkworkplace.com</li>
      <li><svg viewBox="0 0 12 12"><path d="M6 0.5l5.5 5h-1.5v6h-3v-4h-2v4h-3v-6H.5z"/></svg>1480 Harbor Rd. Dallas, TX 75219</li>
    </ul>
  </section>

  <section class="card card-back" aria-label="Business card back">
    <div class="back-brand">LUMARK</div>
  </section>
</body>
</html>
```